Plakat-Design für Vereinsfest
Zielgruppe
Unser Verein veranstaltet jedes Jahr im August das Vereinsfest 'Sonnwendtag', das in einem kleinen Wäldchen innerhalb des Heimatortes stattfindet. Am Samstag und Sonntag sorgen verschiedene Musikgruppen für Unterhaltung. Es soll ein Veranstaltungsplakat gestaltet werden, dass sich an die Vorgaben (siehe unten) hält und die Veranstaltung bewirbt.
Zielgruppe sind Bürger des Heimatortes.
Aufgabenstellung
Das Vereinslogo ist beigefügt und sollte prominent auf dem Plakat vertreten sein, Logo und Schriftzug können auch getrennt oder anders angeordnet werden. Der Veranstaltungstitel lautet "Sonnwendtag", es findet am 20. und 21. August "Am Hirtenstein" (Veranstaltungsort) statt.
Programmpunkte: Samstag: Musikalische Unterhaltung mit den Bachpfeifern; Sonntag: Musikalische Unterhaltung mit den Moorbachrabauken
Uhrzeiten sollten enthalten sein:
Beginn Samstag: ab 15 Uhr
Beginn Sonntag: ab 10 Uhr
Das Plakat soll gut leserlich auch aus der Entfernung sein, da es an Straßen plakatiert wird.
Das Plakat soll für spätere Jahre editierbar sein.
Schriftart im Logo: Californian FB Bold (muss aber nicht auf andere Textelemente angewendet werden). Das Plakat soll in DIN A2 gedruckt werden. Die Webadresse sollte auf dem Plakat stehen.

```html
<!DOCTYPE html>
<html lang="de">
<head>
<meta charset="utf-8">
<title>Sonnwendtag – Plakat</title>
<link href="https://fonts.googleapis.com/css2?family=Cinzel:wght@500;600;700&family=Crimson+Text:wght@600;700&family=Tinos:wght@400;700&display=swap" rel="stylesheet">
<style>
  :root {
    --page-bg: #e9e8e6;
    --paper: #e6edf7;
    --paper-deep: #cfdcee;
    --royal: #0d5d99;
    --royal-light: #1a86c4;
    --royal-dark: #0a3f6e;
    --curtain-shadow: #1d4f78;
    --ink-blue: #17578a;
    --ink-grey: #3f3c3a;
    --box-grey: #464646;
    --white: #ffffff;
  }
  * { margin: 0; padding: 0; box-sizing: border-box; }
  html, body { width: 1200px; height: 1194px; overflow: hidden; }
  body { background: var(--page-bg); position: relative; }

  .poster {
    position: absolute; left: 190px; top: 17px;
    width: 820px; height: 1160px;
    background: linear-gradient(180deg, var(--paper) 0%, var(--paper-deep) 100%);
    overflow: hidden;
  }
  .frame-line { position: absolute; border: 2px solid var(--ink-blue); }
  .frame-outer { left: 32px; right: 32px; top: 300px; bottom: 18px; }
  .frame-inner { left: 42px; right: 42px; top: 310px; bottom: 28px; border-width: 1px; }

  .curtain { position: absolute; left: 0; top: 0; width: 820px; height: 480px; }

  .artwork { position: absolute; border-radius: 6px; }
  .musicians { left: 195px; top: 80px; width: 430px; height: 195px;
    background: linear-gradient(180deg, rgba(255,255,255,.55), rgba(255,255,255,.75)); }
  .notes-left { left: 20px; top: 22px; width: 170px; height: 200px;
    background: linear-gradient(135deg, rgba(255,255,255,.35), rgba(255,255,255,.08)); }
  .notes-right { left: 630px; top: 10px; width: 175px; height: 230px;
    background: linear-gradient(225deg, rgba(255,255,255,.35), rgba(255,255,255,.08)); }
  .ornament-left { left: 50px; bottom: 36px; width: 130px; height: 140px;
    background: linear-gradient(45deg, rgba(23,87,138,.35), rgba(23,87,138,.05)); }
  .ornament-right { right: 50px; bottom: 36px; width: 130px; height: 140px;
    background: linear-gradient(-45deg, rgba(23,87,138,.35), rgba(23,87,138,.05)); }

  .event-title {
    position: absolute; left: 0; right: 0; top: 288px;
    text-align: center; color: var(--white);
    font-family: 'Cinzel', 'Times New Roman', serif; font-weight: 600;
    font-size: 76px; line-height: 1; letter-spacing: 1px;
  }
  .event-title .initial { font-size: 98px; }

  .date {
    position: absolute; left: 0; right: 0; top: 500px; text-align: center;
    color: var(--ink-blue); font-family: 'Cinzel', 'Times New Roman', serif; font-weight: 700;
    font-size: 66px; line-height: 1;
  }
  .venue {
    position: absolute; left: 0; right: 0; top: 582px; text-align: center;
    color: var(--ink-blue); font-family: 'Cinzel', 'Times New Roman', serif; font-weight: 700;
    font-size: 44px; line-height: 1;
  }
  .venue .initial { font-size: 54px; }

  .programme { position: absolute; left: 60px; right: 60px; top: 665px; text-align: center; }
  .programme .day {
    font-family: 'Tinos', 'Times New Roman', serif; font-weight: 700;
    color: var(--ink-grey); font-size: 30px; line-height: 1.05;
  }
  .programme .act {
    font-family: 'Crimson Text', Georgia, serif; font-weight: 700;
    color: var(--ink-blue); font-size: 27px; line-height: 1.15; margin-bottom: 6px;
  }

  .start-times {
    position: absolute; left: 210px; width: 400px; top: 880px; padding: 14px 0;
    background: var(--box-grey); color: var(--white); text-align: center;
    font-family: 'Crimson Text', Georgia, serif; font-weight: 600;
    font-size: 29px; line-height: 1.2;
  }

  .club-name {
    position: absolute; left: 200px; right: 200px; top: 1012px; text-align: center;
    font-family: 'Crimson Text', Georgia, serif; font-weight: 700;
    color: var(--ink-blue); font-size: 32px; line-height: 1.15;
  }

  .website {
    position: absolute; left: 0; right: 0; top: 1100px; text-align: center;
    font-family: 'Tinos', 'Times New Roman', serif; font-weight: 700;
    color: var(--ink-grey); font-size: 26px;
  }
</style>
</head>
<body>
<main class="poster">
  <div class="frame-line frame-outer"></div>
  <div class="frame-line frame-inner"></div>

  <svg class="curtain" viewBox="0 0 820 480" aria-hidden="true">
    <defs>
      <radialGradient id="curtainFill" cx="0.5" cy="0.55" r="0.7">
        <stop offset="0" stop-color="#1a86c4"/>
        <stop offset="0.6" stop-color="#0d5d99"/>
        <stop offset="1" stop-color="#0a3f6e"/>
      </radialGradient>
    </defs>
    <path fill="#1d4f78" d="M0 0 H820 V360 Q790 395 755 380 Q715 455 615 445 Q560 490 410 482 Q260 490 205 445 Q105 455 65 380 Q30 395 0 360 Z"/>
    <path fill="url(#curtainFill)" d="M0 0 H820 V330 Q790 365 758 352 Q720 425 620 418 Q560 465 410 458 Q260 465 200 418 Q100 425 62 352 Q30 365 0 330 Z"/>
  </svg>

  <div class="artwork notes-left" role="img" aria-label="Notenlinien mit Violinschlüssel und Noten"></div>
  <div class="artwork notes-right" role="img" aria-label="Geschwungene Notenlinien mit Noten"></div>
  <div class="artwork musicians" role="img" aria-label="Weiße Silhouetten einer Blaskapelle mit Saxofon, Trompeten und Tuba"></div>

  <h1 class="event-title"><span class="initial">S</span>ONNWENDTAG</h1>

  <p class="date">20 - 21 AUGUST</p>
  <p class="venue">“<span class="initial">A</span>M <span class="initial">H</span>IRTENSTEIN”</p>

  <section class="programme">
    <p class="day">SAMSTAG:</p>
    <p class="act">Musikalische Unterhaltung mit den Bachpfeifern</p>
    <p class="day">SONNTAG:</p>
    <p class="act">Musikalische Unterhaltung mit den<br>Moorbachrabauken</p>
  </section>

  <div class="start-times">
    Beginn Samstag: ab 15 Uhr<br>
    Beginn Sonntag: ab 10 Uhr
  </div>

  <div class="artwork ornament-left" role="img" aria-label="Verschnörkeltes Eckornament"></div>
  <div class="artwork ornament-right" role="img" aria-label="Verschnörkeltes Eckornament"></div>

  <p class="club-name">Heimatverein<br>Tannenried e.V.</p>

  <p class="website">www.heimatverein-tannenried.de</p>
</main>
</body>
</html>
```